Awesome new dental practice requires a New Letterhead design

We would like a new letterhead design to align with our new business branding & business cards. I have uploaded all the logos & current business card details that can be used. The new website can be viewed here https://kelvora.com.au

Other useful details: Font Poppins
Colour Palettes:
Dark Pink #c45389
Light Pink: #e83e8c
Black

Please let me know if you have any questions or require anything else.

Dental

• Poppins

```html
<!DOCTYPE html>
<html lang="en">
<head>
<meta charset="utf-8">
<title>Kelvora Letterhead</title>
<link href="https://fonts.googleapis.com/css2?family=Poppins:ital,wght@0,400;0,500;0,600;1,500;1,600&display=swap" rel="stylesheet">
<style>
  :root {
    --pink-dark: #c45389;
    --pink-light: #e83e8c;
    --ink: #231f20;
    --navy: #1c2340;
    --board: #ced3d7;
    --paper: #ffffff;
  }
  * { margin: 0; padding: 0; box-sizing: border-box; }
  html, body { width: 1200px; height: 1200px; overflow: hidden; }
  body {
    position: relative;
    background: var(--paper);
    font-family: "Poppins", sans-serif;
  }
  .board-title {
    position: absolute; left: 0; top: 0; width: 1200px; height: 151px;
    display: flex; flex-direction: column; align-items: center; justify-content: center;
    color: var(--pink-dark); font-weight: 600; font-size: 26px; line-height: 42px;
    padding-top: 2px;
  }
  .board {
    position: absolute; left: 0; top: 151px; width: 1200px; height: 1049px;
    background: var(--board);
  }
  .letterhead {
    position: absolute; left: 256px; top: 190px; width: 689px; height: 968px;
    background: var(--paper);
    box-shadow: 0 0 6px rgba(0,0,0,0.25);
    overflow: hidden;
  }
  .brand {
    position: absolute; left: 33px; top: 30px;
    display: flex; align-items: center; gap: 8px;
  }
  .brand-mark { width: 10px; height: 10px; background: var(--pink-dark); }
  .brand-name {
    font-weight: 600; font-size: 36px; line-height: 1; color: var(--pink-dark);
    letter-spacing: -0.5px;
  }
  .contact {
    position: absolute; left: 476px; top: 28px;
    color: var(--ink); font-size: 12px; line-height: 22.5px;
  }
  .contact-row { display: flex; align-items: center; }
  .contact-row svg { width: 12px; height: 12px; margin-right: 13px; flex: none; }
  .address {
    margin-top: 5px; color: var(--navy); font-weight: 500; font-size: 12px; line-height: 18.5px;
  }
  .footer { position: absolute; left: 0; bottom: 0; width: 689px; height: 37px; }
  .footer svg { position: absolute; left: 0; top: 0; }
  .tagline {
    position: absolute; right: 33px; top: 7px;
    color: #fff; font-style: italic; font-weight: 500; font-size: 14.5px; line-height: 18px;
  }
  .tagline strong { color: #000; font-weight: 600; }
</style>
</head>
<body>
  <header class="board-title">
    <p>Letterhead- Mockup 1 -Rev-2</p>
    <p>Size: A4, Color Mode : CMYK, Background Color- White</p>
  </header>
  <div class="board"></div>

  <section class="letterhead">
    <div class="brand">
      <span class="brand-mark"></span>
      <span class="brand-name">kelvora</span>
    </div>

    <div class="contact">
      <div class="contact-row">
        <svg viewBox="0 0 24 24"><path fill="#e83e8c" d="M6.6 10.8a15.1 15.1 0 0 0 6.6 6.6l2.2-2.2a1 1 0 0 1 1-.25 11.4 11.4 0 0 0 3.6.57 1 1 0 0 1 1 1V20a1 1 0 0 1-1 1A17 17 0 0 1 3 4a1 1 0 0 1 1-1h3.5a1 1 0 0 1 1 1c0 1.25.2 2.450.57 3.57a1 1 0 0 1-.25 1z"/></svg>
        <span>(08) 9000 4821</span>
      </div>
      <div class="contact-row">
        <svg viewBox="0 0 24 24"><rect x="2" y="5" width="20" height="14" rx="1.5" fill="#e83e8c"/><path d="M3 6.5l9 6 9-6" fill="none" stroke="#fff" stroke-width="2"/></svg>
        <span>hello@kelvora.com.au</span>
      </div>
      <div class="contact-row">
        <svg viewBox="0 0 24 24"><g fill="none" stroke="#e83e8c" stroke-width="2"><circle cx="12" cy="12" r="9"/><ellipse cx="12" cy="12" rx="4" ry="9"/><path d="M3 12h18M5 7h14M5 17h14"/></g></svg>
        <span>www.kelvora.com.au</span>
      </div>
      <p class="address">Shop 9, 28 Wattle Street,<br>Marlow Bay, WA 6099</p>
    </div>

    <footer class="footer">
      <svg width="689" height="37" viewBox="0 0 689 37">
        <path fill="#c45389" d="M0 25 H296 C312 25 322 0 337 0 H689 V37 H0 Z"/>
      </svg>
      <p class="tagline">Life is short, <strong>Smile</strong> while you still have teeth</p>
    </footer>
  </section>
</body>
</html>
```